Skydiving Sports Club Needs Infographic For Donation Support

We are a non for profit sports club organization in the field of skydiving, being such an organization allows us to take donations in order to stain our activity.
We need a "infographic" in order to quickly and clearly explain why people should donate to us, what is the legal framework for it and what we can offer them in exchange for being a club sponsor.
The target audience for this infographic are companies not individual persons. The reason for this is because according to the national fiscal code it is very attractive for companies to make donations to organizations such as ours.
A company may donate 20% out of the amount of money they would pay as "income tax" at the end of the year, but that ammount may not represent more than 0.3% out of that company's turnover for that same year.
The important point being that as long as a company turns a profit the amount of money described above either goes to the state budget in the form of taxes or to an organizations such as ours in the form of donations. The company can't hold on to that money no matter how much they might like to so they might as well give it to us since it doesn't incur any cost towards the company and they also get something in return if they become our sponsors.
Based on the ammount of money they donate we can offer them anything from tandem jumps for their employees organized in events such as team buildings to their branding on our equipment and aircraft for marketing purposes or anything else they might think of and is in direct relation to skydiving and within the rule law.
It's important to make the viewer aware of the fact that we are a club under the NRFA system http://www.nrfa-example.org/ all our operations are conducted at that standard, which is recongniezd to be the safest and most widely spread in the world.
Also skydiving is currently growing exponentially in popularity world wide http://www.nrfa-example.org/Portals/0/Downloads/PR_skydivingcontinuestosoar.pdf and it's a very visual intensive activitiy with a lot of skydiver videos being uploaded on the interent so the potencial marketing exposure for branding of aircarft or equipment is quite large.
our website: www.vantafly.ro
fb page: https://www.facebook.com/vantafly.ro
Target Market(s)
The target audience for this infographic are companies.
Industry/Entity Type
Marketing
Look and feel

```html
<!DOCTYPE html>
<html lang="en">
<head>
<meta charset="utf-8">
<title>VantaFly Skydiving Club – Donation Infographic</title>
<link href="https://fonts.googleapis.com/css2?family=Jost:wght@400;500;600&family=Orbitron:wght@800&display=swap" rel="stylesheet">
<style>
  :root {
    --bg: #ffffff;
    --box: #7f9aab;
    --panel: #4a494c;
    --arrow: #7b7b7b;
    --ink-light: #ffffff;
    --ink-grey: #6a6a6a;
    --ink-dark: #111111;
    --ghost: #605f63;
  }
  * { box-sizing: border-box; margin: 0; padding: 0; }
  html, body { width: 1200px; height: 1000px; overflow: hidden; background: var(--bg); }
  body { font-family: "Jost", sans-serif; }
  .canvas { position: relative; width: 1200px; height: 1000px; }
  .abs { position: absolute; }
  .panel { position: absolute; background: var(--panel); border-radius: 24px; }
  .box {
    position: absolute; background: var(--box); color: var(--ink-light);
    display: flex; align-items: center; justify-content: center; text-align: center;
    font-size: 19px; line-height: 1.25;
  }
  .links { top: 132px; font-size: 17px; color: var(--ink-grey); letter-spacing: .2px; }
  .panel-label { left: 490px; top: 302px; color: var(--ink-light); font-size: 19px; line-height: 1.25; }
  .popularity { flex-direction: column; gap: 4px; font-size: 19px; line-height: 1.3; padding: 10px; }
  .popularity .stat { color: var(--ink-dark); font-size: 23px; margin: 6px 0; }
  .popularity .stat b { font-family: "Orbitron", sans-serif; font-weight: 800; font-size: 23px; }
  .vertical-note {
    left: 186px; top: 384px; width: 200px; transform: rotate(-90deg); transform-origin: center;
    color: var(--ink-grey); font-size: 17px; text-align: center; white-space: nowrap;
  }
  .diamond-label { left: 907px; top: 450px; width: 100px; text-align: center; color: var(--ink-light); font-size: 18px; line-height: 1.25; }
  .option { top: 410px; color: var(--ink-grey); }
  .option h3 { font-weight: 400; font-size: 19px; }
  .option ul { list-style: none; font-size: 9px; color: #333; line-height: 1.4; margin-top: 3px; }
  .option li::before { content: "●"; margin-right: 4px; font-size: 7px; }
  .club-name { left: 776px; top: 604px; width: 160px; text-align: center; font-size: 42px; font-weight: 600; color: #3f8fc6; letter-spacing: -.5px; }
  .club-note { left: 760px; top: 672px; width: 170px; text-align: center; font-size: 16px; color: #555; line-height: 1.25; }
  .member-badge { left: 807px; top: 719px; width: 76px; height: 76px; border-radius: 50%; background: #3d5a8c; }
  .assoc { flex-direction: column; font-size: 16px; line-height: 1.2; }
  .assoc .name { font-size: 18px; }
  .fact { flex-direction: column; justify-content: flex-start; padding-top: 4px; }
  .fact h4 { font-weight: 400; font-size: 19px; line-height: 1.2; }
  .fact ul { list-style: none; font-size: 9px; text-align: left; margin-top: 6px; line-height: 1.35; width: 100%; padding-left: 8px; }
  .benefit { font-size: 18px; padding: 8px; align-items: flex-start; padding-top: 20px; line-height: 1.35; }
  .ghost-title {
    left: 362px; top: 628px; color: var(--ghost); font-size: 40px; text-align: center;
    transform: rotate(-22deg); line-height: 1.15;
  }
  .panel-caption { left: 152px; top: 824px; color: var(--ink-light); font-size: 20px; white-space: nowrap; }
  .arrows { position: absolute; left: 0; top: 0; pointer-events: none; }
  .arrows path, .arrows polyline, .arrows line { fill: none; stroke: var(--arrow); stroke-width: 3; }
</style>
</head>
<body>
<div class="canvas">
  <div class="abs links" style="left:25px;">www.vantafly.ro</div>
  <div class="abs links" style="left:183px;">www.friendnet.com/vantafly.ro</div>

  <div class="panel" style="left:467px; top:155px; width:697px; height:207px;"></div>
  <div class="box" style="left:77px; top:175px; width:356px; height:36px;">Team Building</div>
  <div class="box" style="left:217px; top:233px; width:216px; height:36px;">Branding</div>
  <div class="box" style="left:502px; top:168px; width:232px; height:46px;">Human Resource</div>
  <div class="box" style="left:502px; top:226px; width:234px; height:46px;">Marketing</div>
  <div class="box" style="left:770px; top:167px; width:370px; height:100px; align-items:flex-start; padding-top:40px;">Operations</div>
  <div class="box" style="left:770px; top:311px; width:370px; height:40px;">Revenue with Profit</div>
  <div class="abs panel-label">Company /<br>Organization</div>

  <div class="box popularity" style="left:312px; top:383px; width:342px; height:178px;">
    <div>Widespread Popularity and<br>membership for SkyDiving</div>
    <div class="stat"><b>3.2 million</b> sky dives in 2013</div>
    <div>Large number of videos uploaded<br>on web provides large branding scope</div>
  </div>
  <div class="abs vertical-note">Visual intensive activity</div>

  <svg class="abs" style="left:883px; top:405px;" width="148" height="142" aria-hidden="true">
    <polygon points="74,0 148,71 74,142 0,71" fill="#7f9aab"/>
  </svg>
  <div class="abs diamond-label">Annual Tax Liabilities</div>
  <div class="abs option" style="left:760px;"><h3>Option 2</h3><ul><li>Potential Return Benefits</li><li>Better Alternative for taxes</li></ul></div>
  <div class="abs option" style="left:1038px;"><h3>Option 1</h3><ul><li>No Return Benefits</li><li>Conventional Procedure</li></ul></div>
  <div class="box" style="left:770px; top:539px; width:153px; height:46px;">Donations</div>
  <div class="box" style="left:997px; top:539px; width:154px; height:42px;">Taxes</div>

  <div class="abs club-name">VantaFly</div>
  <div class="abs club-note">Not for Profit sports<br>club organization</div>
  <div class="abs member-badge"></div>

  <div class="box assoc" style="left:1008px; top:617px; width:133px; height:68px;"><span class="name">NRFA</span>National Regional<br>Freefall Association</div>
  <div class="box fact" style="left:962px; top:735px; width:109px; height:110px;">
    <h4>Safety<br>Standards</h4>
    <ul><li>Certified skydiving instructors</li><li>Annual Safety Day</li><li>Seminars and training</li></ul>
  </div>
  <div class="box fact" style="left:1082px; top:735px; width:109px; height:110px;">
    <h4>Wide<br>Coverage</h4>
    <ul><li>36,000 members</li><li>3.2 million jumps</li><li>240 skydiving schools</li></ul>
  </div>

  <div class="panel" style="left:33px; top:577px; width:717px; height:280px;"></div>
  <div class="abs ghost-title">Sponsorship<br>Benefits</div>
  <div class="box benefit" style="left:57px; top:591px; width:131px; height:178px;">Tandem jumps for employees organized in events such as team buildings</div>
  <div class="box benefit" style="left:215px; top:591px; width:131px; height:178px;">Branding on equipments and aircraft for marketing purpose</div>
  <div class="box benefit" style="left:603px; top:591px; width:131px; height:178px;">Support in direct relation to skydiving and within the rule law</div>
  <div class="abs panel-caption">Sponsorship Benefits offered by club based on the donation amount</div>

  <svg class="arrows" width="1200" height="1000" aria-hidden="true">
    <defs>
      <marker id="head" viewBox="0 0 12 12" refX="10" refY="6" markerWidth="6" markerHeight="6" orient="auto">
        <path d="M1,1 L10,6 L1,11" style="stroke:#7b7b7b; stroke-width:2.4; fill:none;"/>
      </marker>
    </defs>
    <line x1="433" y1="192" x2="498" y2="192" marker-end="url(#head)"/>
    <line x1="433" y1="250" x2="498" y2="250" marker-end="url(#head)"/>
    <line x1="734" y1="192" x2="766" y2="192" marker-end="url(#head)"/>
    <line x1="736" y1="250" x2="766" y2="250" marker-end="url(#head)"/>
    <line x1="952" y1="267" x2="952" y2="307" marker-end="url(#head)"/>
    <line x1="957" y1="351" x2="957" y2="401" marker-end="url(#head)"/>
    <polyline points="883,476 826,476 826,535" marker-end="url(#head)"/>
    <polyline points="1031,476 1075,476 1075,535" marker-end="url(#head)"/>
    <line x1="1006" y1="634" x2="940" y2="634" marker-end="url(#head)"/>
    <line x1="1024" y1="685" x2="1024" y2="731" marker-end="url(#head)"/>
    <line x1="1122" y1="685" x2="1122" y2="731" marker-end="url(#head)"/>
    <line x1="123" y1="591" x2="123" y2="215" marker-end="url(#head)"/>
    <line x1="265" y1="591" x2="265" y2="273" marker-end="url(#head)"/>
    <line x1="678" y1="591" x2="678" y2="366" marker-end="url(#head)"/>
    <line x1="310" y1="512" x2="270" y2="512" marker-end="url(#head)"/>
    <polyline points="845,797 845,822 123,822 123,773" marker-end="url(#head)"/>
    <line x1="270" y1="822" x2="270" y2="773" marker-end="url(#head)"/>
    <line x1="668" y1="822" x2="668" y2="773" marker-end="url(#head)"/>
  </svg>
</div>
</body>
</html>
```